Cybersecurity company is looking for business card.

I need a business card design for our company, we are a cybersecurity company providing advance technology to protect agains any kind of malware. We need a fresh modern design it should communicate modern, technology and growth.

Target Market(s)

Business to business

Industry/Entity Type

Business

Contact Information for Business Card

Should have location, address, fax, mobile, phone, email and website.

Requirements
Must have
• Must follow company's logo color and style. Must have the company's log on its.

```html
<!DOCTYPE html>
<html lang="en">
<head>
<meta charset="utf-8">
<title>Vantrel Business Card</title>
<link rel="stylesheet" href="https://fonts.googleapis.com/css2?family=Open+Sans:wght@400;600&display=swap">
<style>
  :root {
    --backdrop: #e9e4dc;
    --card-white: #ffffff;
    --card-grey-light: #f4f4f4;
    --card-grey-dark: #cfcfcf;
    --panel-black: #1b1b1b;
    --panel-black-soft: #3a3a3a;
    --ink: #111111;
    --ink-soft: #444444;
    --text-light: #f2f2f2;
    --rule: #8a8a8a;
  }
  * { box-sizing: border-box; margin: 0; padding: 0; }
  html, body {
    width: 1200px; height: 902px; overflow: hidden;
    background: var(--backdrop);
    font-family: "Open Sans", Arial, sans-serif;
  }
  .stage { position: relative; width: 1200px; height: 902px; }

  .card {
    position: absolute; top: 301px;
    width: 520px; height: 300px;
    border-radius: 24px; overflow: hidden;
    box-shadow: 0 10px 28px rgba(0,0,0,0.22);
  }

  /* Shared company name */
  .brand-name {
    font-family: "Open Sans", Arial, sans-serif;
    font-weight: 600; color: var(--ink); line-height: 1;
    white-space: nowrap;
  }

  /* Front */
  .card-front {
    left: 50px;
    background: radial-gradient(ellipse at 40% 45%, var(--card-white) 0%, var(--card-grey-light) 45%, var(--card-grey-dark) 100%);
  }
  .card-front .brand-name { position: absolute; left: 110px; top: 112px; font-size: 54px; }
  .front-rule {
    position: absolute; left: 40px; right: 40px; top: 214px;
    height: 1px; background: var(--rule);
  }
  .front-url {
    position: absolute; right: 60px; top: 224px;
    font-size: 17px; color: var(--ink-soft); letter-spacing: 0.5px;
  }

  /* Back */
  .card-back { left: 630px; background: var(--card-white); }
  .back-top {
    position: absolute; left: 0; top: 0; width: 100%; height: 150px;
    background: linear-gradient(160deg, var(--panel-black-soft) 0%, var(--panel-black) 55%);
    color: var(--text-light);
  }
  .back-notch {
    position: absolute; left: 46px; top: 149px; width: 0; height: 0;
    border-left: 9px solid transparent; border-right: 9px solid transparent;
    border-top: 9px solid var(--panel-black);
  }
  .person { position: absolute; left: 34px; top: 38px; }
  .person-name { font-size: 24px; font-weight: 400; letter-spacing: 0.5px; line-height: 1.2; }
  .person-title { font-size: 13px; margin-top: 4px; color: #cccccc; }
  .contact-list {
    position: absolute; left: 250px; top: 22px;
    list-style: none; font-size: 13.5px;
  }
  .contact-list li { display: flex; align-items: center; gap: 10px; height: 21px; }
  .contact-list svg { width: 13px; height: 13px; fill: var(--text-light); flex: none; }

  .card-back .brand-name { position: absolute; left: 34px; top: 190px; font-size: 40px; }
  .address {
    position: absolute; left: 270px; top: 196px;
    display: flex; gap: 8px; font-size: 14px; color: var(--ink); line-height: 1.35;
  }
  .address svg { width: 13px; height: 17px; fill: var(--ink); flex: none; margin-top: 2px; }
</style>
</head>
<body>
<main class="stage">

  <section class="card card-front" aria-label="Card front">
    <p class="brand-name">vantrel</p>
    <div class="front-rule"></div>
    <p class="front-url">www.vantrel.com</p>
  </section>

  <section class="card card-back" aria-label="Card back">
    <div class="back-top">
      <div class="person">
        <p class="person-name">YOUR NAME</p>
        <p class="person-title">Title</p>
      </div>
      <ul class="contact-list">
        <li>
          <svg viewBox="0 0 24 24" aria-hidden="true"><path d="M6.6 10.8a15.1 15.1 0 0 0 6.6 6.6l2.2-2.2a1 1 0 0 1 1-.25 11.4 11.4 0 0 0 3.6.57 1 1 0 0 1 1 1V20a1 1 0 0 1-1 1A17 17 0 0 1 3 4a1 1 0 0 1 1-1h3.5a1 1 0 0 1 1 1c0 1.250.2 2.45.57 3.57a1 1 0 0 1-.25 1z"/></svg>
          <span>(03) 5550 1234</span>
        </li>
        <li>
          <svg viewBox="0 0 24 24" aria-hidden="true"><path d="M7 1h10a2 2 0 0 1 2 2v18a2 2 0 0 1-2 2H7a2 2 0 0 1-2-2V3a2 2 0 0 1 2-2zm0 3v14h10V4zm5 15.5a1 1 0 1 0 0 2 1 1 0 0 0 0-2z"/></svg>
          <span>+44 203 555 0142</span>
        </li>
        <li>
          <svg viewBox="0 0 24 24" aria-hidden="true"><path d="M6 2h10l2 2v5h2a2 2 0 0 1 2 2v8h-4v3H6v-3H2v-8a2 2 0 0 1 2-2h2zm2 2v5h8V5h-1V4zm0 11v5h8v-5z"/></svg>
          <span>+44 203 555 0142</span>
        </li>
        <li>
          <svg viewBox="0 0 24 24" aria-hidden="true"><path d="M2 4h20v16H2zm2 2v.5l8 5.5 8-5.5V6zm0 2.9V18h16V8.9l-8 5.5z"/></svg>
          <span>info@vantrel.com</span>
        </li>
        <li>
          <svg viewBox="0 0 24 24" aria-hidden="true"><path d="M12 2a10 10 0 1 0 0 20 10 10 0 0 0 0-20zm6.9 6h-3a15 15 0 0 0-1.3-3.9A8 8 0 0 1 18.9 8zM12 4c.8 1.1 1.5 2.5 1.9 4h-3.8c.4-1.5 1.1-2.9 1.9-4zM4.3 14a8 8 0 0 1 0-4h3.4a16 16 0 0 0 0 4zm.8 2h3a15 15 0 0 0 1.3 3.9A8 8 0 0 1 5.1 16zm3-8h-3a8 8 0 0 1 4.3-3.9A15 15 0 0 0 8.1 8zM12 20c-.8-1.1-1.5-2.5-1.9-4h3.8c-.4 1.5-1.1 2.9-1.9 4zm2.3-6H9.7a14 14 0 0 1 0-4h4.6a14 14 0 0 1 0 4zm.3 5.9a15 15 0 0 0 1.3-3.9h3a8 8 0 0 1-4.3 3.9zm1.7-5.9a16 16 0 0 0 0-4h3.4a8 8 0 0 1 0 4z"/></svg>
          <span>www.vantrel.com</span>
        </li>
      </ul>
    </div>
    <div class="back-notch"></div>

    <p class="brand-name">vantrel</p>

    <div class="address">
      <svg viewBox="0 0 16 22" aria-hidden="true"><path d="M8 0a8 8 0 0 0-8 8c0 6 8 14 8 14s8-8 8-14a8 8 0 0 0-8-8zm0 11a3 3 0 1 1 0-6 3 3 0 0 1 0 6z"/></svg>
      <p>1472 North Cedar Ridge Rd<br>Suite 210-318 Alder Falls, AZ</p>
    </div>
  </section>

</main>
</body>
</html>
```